Packaging Design Project

Looking for a design for 2 chocolate box covers.
Dimensions: 7.5" x 7.5" x 1 .25"
5.75" x 5.75" x 1.25"
Desgn should be only 2 colors.

Visit our website to see our product:
www.lumarocacocoa.com
find us on facebook

Please see these guidelines for artwork on boxes:

Industry/Entity Type

Product

Requirements
Must have
• our logo as seen on our website

```html
<!DOCTYPE html>
<html lang="en">
<head>
<meta charset="utf-8">
<title>Lumaroca Cocoa — Box Cover</title>
<link rel="stylesheet" href="https://fonts.googleapis.com/css2?family=Cormorant+Garamond:wght@500&family=Questrial&display=swap">
<style>
  :root {
    --cocoa-dark: #3e2113;
    --cocoa-deep: #341b0e;
    --cocoa-mid: #5a3419;
    --caramel: #8c5b2f;
    --caramel-soft: #6a4121;
  }
  html, body {
    margin: 0;
    padding: 0;
    overflow: hidden;
    background: var(--cocoa-dark);
  }
  .box-cover {
    position: relative;
    width: 1200px;
    height: 1194px;
    overflow: hidden;
    background: var(--cocoa-dark);
  }
  .pod-pattern,
  .frame-lines {
    position: absolute;
    inset: 0;
    width: 1200px;
    height: 1194px;
  }
  .name-band {
    position: absolute;
    left: 82px;
    top: 464px;
    width: 1037px;
    height: 221px;
    background: var(--caramel);
    text-align: center;
    color: var(--cocoa-dark);
  }
  .brand-name {
    margin: 0;
    padding-top: 36px;
    font-family: "Cormorant Garamond", Georgia, serif;
    font-weight: 500;
    font-size: 108px;
    line-height: 1;
    letter-spacing: 1px;
  }
  .tagline {
    margin: 14px 0 0;
    font-family: "Questrial", "Century Gothic", sans-serif;
    font-size: 25px;
    letter-spacing: 2px;
    text-transform: uppercase;
  }
  .website {
    position: absolute;
    left: 0;
    right: 0;
    top: 980px;
    margin: 0;
    text-align: center;
    font-family: "Questrial", "Century Gothic", sans-serif;
    font-size: 38px;
    letter-spacing: 1px;
    color: var(--caramel);
  }
</style>
</head>
<body>
<main class="box-cover">
  <svg class="pod-pattern" viewBox="0 0 1200 1194" role="img" aria-label="Repeating line-drawn cocoa pod pattern in caramel on dark brown, filling the whole cover">
    <defs>
      <linearGradient id="pod-sweep" x1="0" y1="0" x2="1" y2="1">
        <stop offset="0%" stop-color="#5c361b"/>
        <stop offset="25%" stop-color="#472815"/>
        <stop offset="50%" stop-color="#5e371b"/>
        <stop offset="75%" stop-color="#472815"/>
        <stop offset="100%" stop-color="#5c361b"/>
      </linearGradient>
      <radialGradient id="pod-glow" cx="50%" cy="50%" r="60%">
        <stop offset="0%" stop-color="#8c5b2f" stop-opacity="0.22"/>
        <stop offset="100%" stop-color="#8c5b2f" stop-opacity="0.06"/>
      </radialGradient>
    </defs>
    <rect width="1200" height="1194" fill="url(#pod-sweep)"/>
    <rect width="1200" height="1194" fill="url(#pod-glow)"/>
  </svg>

  <svg class="frame-lines" viewBox="0 0 1200 1194" aria-hidden="true">
    <g fill="none" stroke="#8c5b2f">
      <rect class="outer-frame" x="68" y="68" width="1063" height="1057" stroke-width="9"/>
      <rect class="inner-frame" x="86" y="86" width="1029" height="1024" stroke-width="4"/>
      <rect class="top-panel" x="117" y="117" width="969" height="333" stroke-width="7"/>
      <rect class="bottom-panel" x="117" y="705" width="969" height="381" stroke-width="7"/>
      <line class="band-rule" x1="82" y1="454" x2="1119" y2="454" stroke-width="4"/>
      <line class="band-rule" x1="82" y1="695" x2="1119" y2="695" stroke-width="4"/>
    </g>
  </svg>

  <section class="name-band">
    <h1 class="brand-name">Lumaroca Cocoa</h1>
    <p class="tagline">Handmade in the Viennese Style</p>
  </section>

  <p class="website">www.lumarocacocoa.com</p>
</main>
</body>
</html>
```